Eyewear store

-The design must be based around the attached HPID (home page information design) called Lens by Harwick HPID. I've attached Word and PDF versions - these are the same. The table boxes are just for approximate placement of information – you DON'T have to box everything in and you can arrange these. All fonts used in the HPID are only examples - you can use any Google font you wish.
- Information only is in orange text. Copy to go on the design in black text. Some instructions are in the HPID. Please be creative!
-The design needs to be modern. Colours are to be brown, green, black and white ...refer to the shop images in the HPID. Keep it clean and simple, don't need to use all the colours.
- I've provided the images for the site but these are just to show style, use any similar images, but they must be free images.
Width of content will be 1100 pixels when implemented as a web page. Header height (without nav bar) 150-160 pixels.
If your design is chosen the winning PSD file will have to be provided as follows…
1. Canvas size of 2000px x 2000px - 72ppi in Adobe Photoshop (CS5 compatible)
2. Width of content section is 1100px wide - centered in the canvas
3. Any button rollovers/hovers in the PSD as hidden layers.
4. All fonts used must be Google fonts (except for the fonts in the header at the top of the page).
5. You will need to supply the chosen home page plus one example page (example page as a style guide for how all other pages will look). Example page is only the header and navigational bar at the top, an empty sector in the middle with a column (180 px wide) which can be left or right aligned which means the main sector is 920 pixels wide, and then the footer at the bottom of the page
Checklist - http://pixelreviewlist.example/
Target Market(s)
Fashion Eyewear lovers
Mid age women
Sportspeople
Teenagers who need prescription
Non-glasses wearers - People looking to buy branded sunglasses (fashion conscious people of all ages)
Industry/Entity Type
Store
Look and feel
Each slider illustrates characteristics of the customer's brand and the style your logo design should communicate.

```html
<!DOCTYPE html>
<html lang="en">
<head>
<meta charset="utf-8">
<title>Lens by Harwick</title>
<link rel="stylesheet" href="https://fonts.googleapis.com/css2?family=Open+Sans:ital,wght@0,300;0,400;0,600;1,400;1,600&display=swap">
<style>
:root{
  --black:#000;
  --ink:#222;
  --white:#fff;
  --lime:#8ccc1f;
  --lime-soft:#b6e06a;
  --moss:#3e5a24;
  --forest:#232f12;
  --grey:#8a8a8a;
  --rule:#bdbdbd;
  --photo-a:#e9e9e9;
  --photo-b:#6b6b6b;
}
*{margin:0;padding:0;box-sizing:border-box}
html,body{width:1200px;height:1200px;overflow:hidden;background:var(--white)}
body{position:relative;font-family:"Open Sans",Arial,sans-serif;color:var(--ink)}
.top-bar{position:absolute;left:0;top:0;width:1200px;height:5px;background:var(--black)}
.site-title{position:absolute;left:0;width:1200px;top:24px;text-align:center;font-size:21px;font-weight:300;color:#333;letter-spacing:.3px}
.main-nav{position:absolute;top:59px;left:285px;display:flex;gap:0;font-size:10px;color:var(--grey)}
.main-nav a{color:inherit;text-decoration:none;margin-right:25px}
.main-nav a.current{color:var(--black)}
.tagline{position:absolute;top:108px;left:0;width:1200px;padding-left:22px;text-align:center;font-size:20px;font-style:italic;font-weight:600;color:var(--lime)}
.tiles{position:absolute;left:270px;top:147px;width:660px;height:550px}
.tile{position:absolute;font-weight:300}
.tile-specs{left:0;top:0;width:330px;height:126px;background:var(--black);color:var(--white)}
.tile-specs .small{position:absolute;left:22px;top:30px;font-size:15px}
.tile-specs .big{position:absolute;left:22px;top:48px;font-size:28px}
.tile-promo{left:330px;top:0;width:330px;height:126px;background:var(--forest);color:var(--white);font-size:32px;line-height:29px;padding:38px 0 0 43px}
.tile-exam{left:0;top:126px;width:330px;height:212px;background:var(--lime);color:var(--white);font-size:32px;line-height:30px;padding:70px 0 0 60px}
.tile-about{left:0;top:338px;width:330px;height:212px;background:var(--moss);color:var(--white);font-size:32px;padding:80px 0 0 65px}
.tile-photo{left:330px;top:126px;width:330px;height:424px;background:linear-gradient(100deg,var(--photo-a) 0%,#cfcfcf 45%,var(--photo-b) 100%)}
.tile-photo .tint{position:absolute;left:0;top:212px;width:330px;height:212px;background:var(--lime-soft);opacity:.85}
.tile-eyewear{left:345px;top:134px;font-size:30px;color:var(--black)}
.tile-new{left:343px;top:398px;font-size:30px;line-height:29px;color:var(--black)}
.feature{position:absolute;top:718px;width:216px}
.feature h2{font-size:11px;font-weight:600;color:#5aa61a;text-align:center;line-height:13px;height:23px;display:flex;align-items:flex-end;justify-content:center}
.feature .pic{margin-top:3px;height:96px;border-top:4px solid var(--black)}
.feature p{font-size:6.6px;line-height:9px;color:#444;padding:10px 14px 0}
.feature p+p{padding-top:6px}
.f1{left:270px}.f2{left:494px}.f3{left:715px;width:205px}
.pic-sun{background:linear-gradient(180deg,#e8dccb,#cbb89b)}
.pic-rx{background:linear-gradient(90deg,#f2ae6a,#f3f3f0 60%,#e6e6e6)}
.pic-exam{background:linear-gradient(180deg,#f5f5f5,#d2d2d2)}
.brands-title{position:absolute;top:940px;left:0;width:1200px;text-align:center;font-size:12px;font-weight:600;letter-spacing:1px;color:#333}
.rule{position:absolute;left:0;width:1200px;height:1px;background:var(--rule)}
.rule.a{top:960px}.rule.b{top:1020px;height:2px}
.brand-row{position:absolute;top:983px;left:445px;display:flex;gap:12px;font-size:9px;font-weight:600;color:var(--grey)}
.brand-row span{border-bottom:1px solid transparent}
.site-footer{position:absolute;left:0;top:1031px;width:1200px;height:169px;background:#111;color:var(--white)}
.footer-nav{position:absolute;left:320px;top:28px;list-style:none;font-size:8px;line-height:12.6px;color:var(--lime)}
.hours{position:absolute;left:520px;top:32px}
.site-footer h3{font-size:16px;font-weight:400;line-height:18px}
.site-footer .info{font-size:7.5px;line-height:10.5px;margin-top:2px}
.address{position:absolute;left:525px;top:106px}
.stores{position:absolute;left:719px;top:30px}
.store{margin-top:6px;width:155px;height:26px;display:flex;align-items:center;gap:6px;padding:0 6px;font-size:9px;font-weight:600}
.store.one{background:#0e2b7a;color:var(--white)}
.store.two{background:var(--white);color:#0e2b7a;margin-top:22px}
.store .dot{width:10px;height:10px;background:currentColor;border-radius:50%}
.view{font-size:7.5px;margin-top:5px;padding-left:1px}
</style>
</head>
<body>
<div class="top-bar"></div>
<header>
  <div class="site-title">Lens by Harwick</div>
  <nav class="main-nav">
    <a class="current">Home</a><a>About</a><a>Eyewear</a><a>Book an Eye Exam</a><a>Specials/Promotions</a><a>All About Eyes</a><a>News</a><a>Articles</a><a>Other Stores</a><a>Contact</a>
  </nav>
</header>
<p class="tagline">For stylish sunglasses, prescription glasses and eye exams in Kerrowdale</p>

<section class="tiles">
  <div class="tile tile-specs"><span class="small">All you need...is the</span><span class="big">right pair of specs</span></div>
  <div class="tile tile-promo">promotions &amp;<br>stores</div>
  <div class="tile tile-exam">book<br>an eye exam</div>
  <div class="tile tile-about">all about eyes</div>
  <div class="tile tile-photo" role="img" aria-label="Black and white photo of a woman wearing dark sunglasses"><div class="tint"></div></div>
  <div class="tile tile-eyewear">eye wear</div>
  <div class="tile tile-new">what's<br>new in store</div>
</section>

<article class="feature f1">
  <h2>Largest sunglasses selection in Kerrowdale</h2>
  <div class="pic pic-sun" role="img" aria-label="Photo of a woman on a beach wearing mirrored sunglasses"></div>
  <p>For the latest brands and designer sunglasses come in and see the friendly team at Lens by Harwick. There's something for everyone with thousands of glasses in store – view our selection online now.</p>
  <p>We're also the exclusive stockist in Kerrowdale of Corvex sunglasses and optical frames.</p>
</article>
<article class="feature f2">
  <h2>Kerrowdale's Prescription glasses experts –perfect fit guaranteed</h2>
  <div class="pic pic-rx" role="img" aria-label="Photo of a red-haired woman in glasses by a bookshelf"></div>
  <p>Lens by Harwick is your One Stop Eyecare store and have a huge range of prescription lenses, contact lenses and the very latest European trend-setting fashion eye-wear.</p>
  <p>Take a look at our selection of prescription glasses now.</p>
</article>
<article class="feature f3">
  <h2>For eye exams in the heart of Kerrowdale</h2>
  <div class="pic pic-exam" role="img" aria-label="Photo of black glasses in front of an eye chart"></div>
  <p>Lens by Harwick offers complete eye examinations in store. Our Optometrists offer free annual check-ups and glasses fitting.</p>
  <p>And all our glasses come with a full replacement warranty on all new frames and lenses sold – Book</p>
</article>

<div class="brands-title">BRANDS</div>
<div class="rule a"></div>
<div class="brand-row"><span>SOLVANE</span><span>Marbello</span><span>Tidewell</span><span>Corvex</span><span>LANNI</span><span>revona</span><span>JAQUEL</span></div>
<div class="rule b"></div>

<footer class="site-footer">
  <ul class="footer-nav">
    <li>Home</li><li>About</li><li>Eyewear</li><li>Book an Eye Exam</li><li>Specials/Promotions</li><li>All About Eyes</li><li>News</li><li>Articles</li><li>Other Stores</li><li>Contact</li>
  </ul>
  <div class="hours">
    <h3>Open hours</h3>
    <p class="info">Monday - Friday 9am - 5pm<br>Saturday - 9am - 1pm<br>Statutory Holidays – closed</p>
  </div>
  <div class="address">
    <h3>Address</h3>
    <p class="info">14B Harbour Lane<br>Kerrowdale 7310<br>New Zealand</p>
  </div>
  <div class="stores">
    <h3>Other Stores</h3>
    <div class="store one"><span class="dot"></span>Kerrowdale Optical House</div>
    <p class="view">View website</p>
    <div class="store two"><span class="dot"></span>Northvale Eyecare</div>
    <p class="view">View website</p>
  </div>
</footer>
</body>
</html>
```